Looking to design a new sign for our church.

Looking for a new sign
4 x 8 feet dimension
We are renaming the church "Medlow Ridge Community Church"
looking for legible graphics
Would like some type of backdrop being a family tree (oak) / open to other ideas as you are led
I have included a pic of the old sign for your review
would like to incorporate our Ridgeline Ministries on the lower right hand corner of the sign / see file attached

```html
<!DOCTYPE html>
<html lang="en">
<head>
<meta charset="utf-8">
<title>Medlow Ridge Community Church — Sign</title>
<link rel="stylesheet" href="https://fonts.googleapis.com/css2?family=Oswald:wght@600&family=Poppins:wght@500;600&display=swap">
<style>
  :root {
    --page: #e8ebef;
    --navy: #1a1f7a;
    --navy-deep: #14186a;
    --sky: #3d9be6;
    --sky-light: #9fd0f5;
    --band: #35a9ec;
    --white: #ffffff;
  }
  * { margin: 0; padding: 0; box-sizing: border-box; }
  html, body {
    width: 1200px; height: 969px; overflow: hidden;
    background: var(--page);
  }
  .sign {
    position: absolute;
    left: 40px; top: 177px;
    width: 1120px; height: 615px;
    overflow: hidden;
    background:
      radial-gradient(circle at 1099px 149px, rgba(255,255,255,0.95) 0 40px, rgba(190,228,255,0.7) 90px, transparent 260px),
      radial-gradient(ellipse 620px 420px at 900px 60px, rgba(61,155,230,0.85), transparent 75%),
      linear-gradient(90deg, #f4f9fe 0%, #ffffff 38%, #dcecfa 62%, #7cbcef 100%);
  }
  .sign__sky {
    position: absolute; inset: 0;
    background: linear-gradient(0deg, rgba(160,205,242,0.55) 0%, transparent 40%);
  }
  .sign__title {
    position: absolute;
    left: 50px; top: 28px;
    font-family: 'Oswald', sans-serif;
    font-weight: 600;
    font-size: 104px;
    line-height: 0.98;
    color: var(--navy);
    letter-spacing: -0.5px;
    text-shadow: 3px 3px 0 var(--sky-light);
  }
  .sign__band {
    position: absolute; left: 0; top: 319px;
  }
  .sign__band-label {
    position: absolute;
    left: 56px; top: 324px;
    font-family: 'Poppins', sans-serif;
    font-weight: 500;
    font-size: 42px;
    line-height: 48px;
    color: var(--white);
    letter-spacing: 0.5px;
  }
  .services {
    position: absolute;
    left: 56px; top: 388px;
    font-family: 'Poppins', sans-serif;
    font-weight: 600;
    font-size: 41px;
    line-height: 51px;
    color: var(--navy);
    list-style: none;
  }
  .services li { white-space: pre; }
  .ministry {
    position: absolute;
    left: 920px; top: 300px;
    width: 170px;
    display: flex; flex-direction: column; align-items: center; gap: 16px;
    font-family: 'Poppins', sans-serif;
    font-weight: 600;
    font-size: 28px;
    line-height: 1.15;
    color: var(--navy);
    text-align: center;
  }
  .ministry__dot {
    width: 90px; height: 90px; border-radius: 50%;
    background: var(--navy);
  }
</style>
</head>
<body>
  <main class="sign">
    <div class="sign__sky" role="img" aria-label="Soft blue sky with sunlight glow"></div>

    <h1 class="sign__title">Medlow Ridge<br>Community Church</h1>

    <svg class="sign__band" width="600" height="56" viewBox="0 0 600 56" aria-hidden="true">
      <polygon points="0,0 525,0 545,56 0,56" fill="var(--band)"/>
      <polygon points="530,0 560,0 590,56 560,56" fill="var(--navy-deep)"/>
    </svg>
    <div class="sign__band-label">CHURCH SERVICES</div>

    <ul class="services">
      <li>Sunday School    -  9:30am</li>
      <li>Worship Service -  10:30am</li>
      <li>Wednesday Service - 6:00pm</li>
    </ul>

    <div class="ministry">
      <span class="ministry__dot"></span>
      <span>Ridgeline Ministries</span>
    </div>
  </main>
</body>
</html>
```